Business card for STEADYWAVE

Please design professional business card for IT consulting firm STEADYWAVE INC.
Use logo attached.
Use information from sample qNode business card attached.
replace qnode inc with STEADYWAVE INC.
as well as qnodeinc.com with steadywave.example

```html
<!DOCTYPE html>
<html lang="en">
<head>
<meta charset="utf-8">
<title>STEADYWAVE Business Card</title>
<link rel="stylesheet" href="https://fonts.googleapis.com/css2?family=Montserrat:wght@400;500;700&family=Oswald:wght@500;600&display=swap">
<style>
  :root {
    --backdrop: #2a2a2a;
    --ink: #000000;
    --paper: #ffffff;
    --teal: #33ffcc;
    --blue: #5b8fe8;
    --purple: #9410d8;
    --orange: #ff9c0f;
  }
  * { box-sizing: border-box; margin: 0; padding: 0; }
  html, body {
    width: 1200px; height: 1015px; overflow: hidden;
    background: radial-gradient(ellipse at center, #3a3a3a 0%, var(--backdrop) 70%, #1a1a1a 100%);
    font-family: "Montserrat", sans-serif;
  }
  .canvas {
    width: 1200px; height: 1015px;
    display: flex; flex-direction: column; align-items: center; justify-content: center; gap: 60px;
  }
  .card {
    width: 700px; height: 400px; position: relative; overflow: hidden;
    box-shadow: 0 10px 30px rgba(0,0,0,.55);
  }

  /* Back side */
  .card-back { background: var(--ink); }
  .card-back .wordmark {
    position: absolute; left: 0; right: 0; top: 50%; transform: translateY(-50%);
    text-align: center; color: var(--paper);
    font-weight: 700; font-size: 52px; letter-spacing: 10px;
  }

  /* Front side */
  .card-front { background: var(--paper); }
  .front-header {
    height: 125px; display: flex; align-items: center; justify-content: center; gap: 14px;
  }
  .front-header .wordmark {
    font-weight: 700; font-size: 46px; letter-spacing: 9px; color: var(--ink);
  }
  .front-header .mark-square { width: 18px; height: 18px; background: var(--purple); }

  .info-band {
    height: 165px; background: var(--ink); color: var(--paper);
    display: flex; align-items: center; padding: 0 36px;
  }
  .person { flex: 1; text-align: right; padding-right: 26px; }
  .person .name {
    font-family: "Oswald", sans-serif; font-weight: 600; font-size: 28px;
    text-transform: uppercase; letter-spacing: .3px; line-height: 1.1;
  }
  .person .role { font-size: 21px; font-weight: 400; letter-spacing: 1px; }
  .divider { width: 1px; height: 110px; background: #888; }
  .contacts { flex: 1.25; padding-left: 22px; list-style: none; font-size: 17px; line-height: 1.45; }
  .contacts li { display: flex; align-items: center; gap: 10px; white-space: nowrap; }
  .contacts svg { width: 18px; height: 18px; flex: none; fill: none; stroke: var(--paper); stroke-width: 1.8; }

  .front-footer { height: 95px; display: flex; flex-direction: column; justify-content: center; align-items: center; }
  .company { font-weight: 700; font-size: 21px; letter-spacing: .5px; color: var(--ink); }
  .address { font-size: 17px; letter-spacing: .6px; color: var(--ink); }

  .color-stripe { position: absolute; left: 0; right: 0; bottom: 0; height: 15px; display: flex; }
  .color-stripe span { flex: 1; }
  .stripe-teal { background: var(--teal); }
  .stripe-blue { background: var(--blue); }
  .stripe-purple { background: var(--purple); }
  .stripe-orange { background: var(--orange); }
</style>
</head>
<body>
<main class="canvas">
  <section class="card card-back">
    <div class="wordmark">STEADYWAVE</div>
  </section>

  <section class="card card-front">
    <header class="front-header">
      <span class="wordmark">STEADYWAVE</span>
      <span class="mark-square"></span>
    </header>

    <div class="info-band">
      <div class="person">
        <p class="name">Dorian Velesko, P.Eng.</p>
        <p class="role">General Manager</p>
      </div>
      <div class="divider"></div>
      <ul class="contacts">
        <li>
          <svg viewBox="0 0 24 24"><path d="M5 3h4l2 5-3 2a11 11 0 0 0 6 6l2-3 5 2v4a2 2 0 0 1-2 2A18 18 0 0 1 3 5a2 2 0 0 1 2-2z"/></svg>
          (905)555-0142 ext.201
        </li>
        <li>
          <svg viewBox="0 0 24 24"><rect x="6" y="2" width="12" height="20" rx="2"/><line x1="11" y1="18" x2="13" y2="18"/></svg>
          (416)555-0187
        </li>
        <li>
          <svg viewBox="0 0 24 24"><rect x="2" y="5" width="20" height="14"/><path d="M2 5l10 8 10-8"/></svg>
          dvelesko@steadywave.example
        </li>
        <li>
          <svg viewBox="0 0 24 24"><circle cx="12" cy="12" r="10"/><ellipse cx="12" cy="12" rx="4" ry="10"/><line x1="2" y1="12" x2="22" y2="12"/></svg>
          www.steadywave.example
        </li>
      </ul>
    </div>

    <footer class="front-footer">
      <p class="company">STEADYWAVE INC.</p>
      <p class="address">2180 Harrow Ln., Suite 204, Oakridge, Ontario, K0A1B0, Canada</p>
    </footer>

    <div class="color-stripe">
      <span class="stripe-teal"></span>
      <span class="stripe-blue"></span>
      <span class="stripe-purple"></span>
      <span class="stripe-orange"></span>
    </div>
  </section>
</main>
</body>
</html>
```